Business Card Design

Vintage looking Hair Salon, where the customer service is 100%. We are based in a cottage. With shabby chic console tables and beautiful ornate mirrors..and rich brown leather cutting chairs. Chandeliers at the window, and a ornate patchwork sofa.
our clientele are 28years upwards.. Mums with small children.. Ladies that lunch, and men that want more than a barbers and are prepared to pay for our services.
I am looking for a classy business card.. That look expensive.. Where our initials WMP become a visual reference.. I was thinking of cream card initials in black on a embossed tarnished silver.. But I'm open to suggestion. I want,  need the design to be able to work with flyers price list ect.

Industry/Entity Type
Business
Contact Information for Business Card
Willow Mane Parlour
17 Fernbrook Lane
Dunmore Green
bN42 6QW
FB thewillowmaneparlour
Info@thewilowmaneparlour.co.uk
0208 761 5924

```html
<!DOCTYPE html>
<html lang="en">
<head>
<meta charset="utf-8">
<title>Willow Mane Parlour – Business Card</title>
<link rel="stylesheet" href="https://fonts.googleapis.com/css2?family=Tinos:wght@400&display=swap">
<style>
  :root {
    --backdrop: #2b2b2b;
    --card-cream: #f1dcc6;
    --card-cream-deep: #e8cfb6;
    --slate: #55616b;
    --ink: #141414;
    --icon-grey: #a19a95;
    --divider: #b9a591;
  }
  * { box-sizing: border-box; margin: 0; padding: 0; }
  html, body {
    width: 1200px; height: 1000px; overflow: hidden;
    background: var(--backdrop);
  }
  .canvas {
    position: relative; width: 1200px; height: 1000px;
  }
  .business-card {
    position: absolute; left: 150px; top: 243px;
    width: 900px; height: 514px;
    border-radius: 40px; overflow: hidden;
    background: var(--card-cream);
    font-family: "Tinos", "Times New Roman", serif;
    box-shadow: 0 14px 40px rgba(0,0,0,0.45);
  }
  .card-texture {
    position: absolute; inset: 0;
    background: radial-gradient(ellipse at 40% 45%, var(--card-cream) 0%, var(--card-cream-deep) 100%);
  }
  .monogram {
    position: absolute; left: 0; top: 0; width: 420px; height: 514px;
    display: flex; align-items: center; justify-content: center;
  }
  .monogram-letters {
    font-size: 112px; color: var(--slate); letter-spacing: 4px; line-height: 1;
  }
  .panel-divider {
    position: absolute; left: 420px; top: 60px; width: 2px; height: 394px;
    background: linear-gradient(to bottom, transparent, var(--divider) 25%, var(--divider) 75%, transparent);
  }
  .details {
    position: absolute; left: 470px; top: 78px; right: 30px;
    color: var(--ink);
  }
  .salon-name {
    font-size: 25px; color: var(--slate); letter-spacing: 2px;
    text-transform: uppercase; font-weight: 400;
  }
  .address {
    margin-top: 22px; font-size: 24px; line-height: 28px; font-style: normal;
  }
  .contact-list {
    list-style: none; margin-top: 34px;
  }
  .contact-item {
    display: flex; align-items: center; gap: 14px;
    height: 44px; font-size: 24px;
  }
  .contact-icon {
    width: 34px; height: 34px; flex: none; display: block;
  }
</style>
</head>
<body>
<main class="canvas">
  <section class="business-card">
    <div class="card-texture" role="img" aria-label="Faint cream damask pattern across the card"></div>

    <div class="monogram">
      <span class="monogram-letters">WMP</span>
    </div>

    <div class="panel-divider"></div>

    <div class="details">
      <h1 class="salon-name">Willow Mane Parlour</h1>
      <address class="address">
        17 Fernbrook Lane Dunmore Green<br>
        Ashcombe, Wexley, BN42 6QW
      </address>
      <ul class="contact-list">
        <li class="contact-item">
          <svg class="contact-icon" viewBox="0 0 34 34" aria-hidden="true">
            <rect x="1" y="1" width="32" height="32" rx="7" fill="var(--icon-grey)"/>
          </svg>
          <span>thewillowmaneparlour</span>
        </li>
        <li class="contact-item">
          <svg class="contact-icon" viewBox="0 0 34 34" aria-hidden="true">
            <circle cx="17" cy="17" r="14" fill="none" stroke="var(--icon-grey)" stroke-width="2"/>
            <ellipse cx="17" cy="17" rx="6" ry="14" fill="none" stroke="var(--icon-grey)" stroke-width="2"/>
            <line x1="3" y1="17" x2="31" y2="17" stroke="var(--icon-grey)" stroke-width="2"/>
            <line x1="6" y1="10" x2="28" y2="10" stroke="var(--icon-grey)" stroke-width="1.5"/>
            <line x1="6" y1="24" x2="28" y2="24" stroke="var(--icon-grey)" stroke-width="1.5"/>
          </svg>
          <span>www.thewillowmaneparlour.co.uk</span>
        </li>
        <li class="contact-item">
          <svg class="contact-icon" viewBox="0 0 34 34" aria-hidden="true">
            <rect x="3" y="8" width="28" height="19" fill="none" stroke="var(--icon-grey)" stroke-width="2"/>
            <polyline points="3,8 17,19 31,8" fill="none" stroke="var(--icon-grey)" stroke-width="2"/>
          </svg>
          <span>Info@thewilowmaneparlour.co.uk</span>
        </li>
        <li class="contact-item">
          <svg class="contact-icon" viewBox="0 0 34 34" aria-hidden="true">
            <rect x="1" y="1" width="32" height="32" rx="7" fill="var(--icon-grey)"/>
            <path d="M11 8 l4 0 l2 6 l-3 2 q2 4 5 6 l2 -3 l6 2 l0 4 q-1 2 -4 2 q-9 -1 -14 -12 q0 -5 2 -7z" fill="var(--card-cream)"/>
          </svg>
          <span>0208 761 5924</span>
        </li>
      </ul>
    </div>
  </section>
</main>
</body>
</html>
```